Promotional brochure required for short term rental management agency based in Portugal

We are a short-term property management agency based in the Algarve region of Portugal (we manage properties for landlords and promote their property on platforms such as Quellory, pivarno.com and other vacation rental sites - and we take care of marketing, guest management, cleaning, maintenance etc.). We need a 5 page brochure template which is aimed at estate agents who will promote our product to potential new leads / the owners of the properties (NOT the holidaymakers who book the properties).The template should be pretty heavy on the visuals, with photos of properties and infographs (graphs displaying potential revenue etc. and bullet points for our USPs) - and the design and colours of the brochure should promote trust in our ability to keep properties immaculately maintained but also that we have the abilities to market the properties to maximise rental revenue.IMPORTANT NOTE - As this template will be amended for all future leads, we need the design to be in a format that we can amend with minimal skill required (just on pages 1, 2 and 6. The other pages remain static) - so Word, Excel or any other format the designer can recommend. We would be happy to pay for a subscription for this e.g. Canva, Visme, Piktochart etc. Page layout as follows -COVER PAGE – Title - ‘PROPERTY REVENUE FORECAST’• Photo and address of property• ‘Prepared by <Name>’• Space for our company logo (still being designed), website, email address, phone numberPAGE 2 – PROPERTY FIGURES• Total expected annual revenue (single figure – Euro amount)• Month by Month revenue (line graph)• Average daily rate forecast (line graph)• Occupancy (line graph)• Average daily rate (single figure – Euro amount)• Annual occupancy rate (single figure - percentage)• ROI (single figure – percentage)PAGE 3 – LANTERNVALE (INTRO & WHY CHOOSE US)Page of text about renting out properties as short term rentals.3 bullets – make more money / stress free / complete flexibilityPAGE 4 – LANTERNVALE SETUP SERVICE• €495 set price7 inclusions / bullet points PAGE 5 – LANTERNVALE PROPERTY MANAGEMENT• 25% set price9 inclusions / bullet points PAGE 6 – BACK PAGE• Alternate property photo• Company contact infoI have attached below the landing page of our website (currently under construction) to give you an idea of colours, fonts, style etc.
Homeowners of properties valued at €200,000+
Usually aged 40+
Property Management

```html
<!DOCTYPE html>
<html lang="en">
<head>
<meta charset="utf-8">
<title>Lanternvale – Property Revenue Forecast Brochure</title>
<link href="https://fonts.googleapis.com/css2?family=Roboto+Slab:wght@400;500;700&display=swap" rel="stylesheet">
<style>
  :root {
    --teal: #1fb5ab;
    --teal-light: #3cc6bb;
    --teal-dark: #17968e;
    --ink: #333638;
    --ink-soft: #5b5f62;
    --paper: #f5f5f5;
    --paper-edge: #e6e6e6;
    --stage: #a9a9a9;
    --grid: #c9d3d8;
    --rose: #f2b8b0;
    --rose-line: #e39a90;
  }
  * { box-sizing: border-box; margin: 0; padding: 0; }
  html, body { width: 1200px; height: 2242px; overflow: hidden; background: var(--stage); }
  body { font-family: "Roboto Slab", Georgia, serif; color: var(--ink); }
  .canvas { position: relative; width: 1200px; height: 2242px; overflow: hidden; }

  .stage-label { position: absolute; font-size: 20px; color: #1e1e1e; transform: translateX(-50%); white-space: nowrap; }

  .page { position: absolute; background: var(--paper); overflow: hidden; box-shadow: 0 2px 6px rgba(0,0,0,.18); }
  .photo { position: absolute; }

  .logo { position: absolute; display: flex; align-items: center; gap: 5px; color: var(--teal); font-weight: 500; white-space: nowrap; }
  .logo-mark { display: inline-block; background: var(--teal); }

  /* cover */
  .cover { left: 172px; top: 117px; width: 386px; height: 564px; }
  .cover .logo { left: 33px; top: 42px; font-size: 19px; }
  .cover .logo-mark { width: 12px; height: 12px; }
  .cover-address { position: absolute; right: 20px; top: 45px; text-align: right; font-size: 9px; line-height: 1.35; color: var(--ink-soft); }
  .cover-address b { color: var(--ink); }
  .cover-tab { position: absolute; left: 352px; top: 105px; width: 34px; height: 190px; background: #a4a6a7; }
  .cover-band { position: absolute; left: 0; top: 164px; width: 352px; height: 130px; background: linear-gradient(90deg, var(--teal), var(--teal-light)); }
  .cover-band-edge { position: absolute; left: 352px; top: 164px; width: 34px; height: 130px; background: var(--teal-dark); }
  .cover-title { position: absolute; left: 35px; top: 182px; font-size: 31px; line-height: 1.22; font-weight: 700; color: #fff; }
  .cover-prepared { position: absolute; left: 35px; top: 268px; font-size: 8.5px; font-weight: 700; color: #fff; }
  .cover-footer { position: absolute; left: 20px; right: 20px; top: 542px; display: flex; gap: 14px; font-size: 8.5px; color: var(--ink-soft); align-items: center; }
  .contact-dot { display: inline-block; width: 9px; height: 9px; border-radius: 50%; background: var(--teal); margin-right: 5px; vertical-align: -1px; }
  .sep { color: #bbb; }

  /* back */
  .back { left: 622px; top: 117px; width: 358px; height: 564px; }
  .back-edge { position: absolute; left: 338px; top: 260px; width: 20px; height: 124px; background: var(--teal-dark); }
  .back-band { position: absolute; left: 0; top: 277px; width: 338px; height: 107px; background: linear-gradient(90deg, var(--teal), var(--teal-light)); }
  .back-title { position: absolute; left: 35px; top: 314px; font-size: 30px; font-weight: 700; color: #fff; }
  .back-prepared { position: absolute; left: 37px; top: 358px; font-size: 8px; font-weight: 700; color: #fff; }
  .back .logo { left: 33px; top: 423px; font-size: 19px; }
  .back .logo-mark { width: 12px; height: 12px; }
  .back-label { position: absolute; left: 33px; top: 459px; font-size: 9px; font-weight: 700; }
  .back-contacts { position: absolute; left: 33px; top: 482px; list-style: none; font-size: 8px; line-height: 1.55; color: var(--ink-soft); }
  .back-contacts .contact-dot { width: 7px; height: 7px; }

  /* inner pages */
  .inner { width: 427px; height: 631px; }
  .p1 { left: 169px; top: 726px; } .p2 { left: 596px; top: 726px; }
  .p3 { left: 169px; top: 1455px; } .p4 { left: 596px; top: 1455px; }
  .run-head { position: absolute; left: 0; top: 0; width: 100%; height: 52px; background: linear-gradient(90deg, var(--teal), var(--teal-light)); color: #fff; display: flex; justify-content: space-between; align-items: center; padding: 0 22px 0 26px; }
  .run-title { font-size: 15px; font-weight: 500; }
  .run-by { font-size: 8px; font-weight: 700; }
  .run-foot { position: absolute; left: 22px; right: 22px; bottom: 14px; height: 22px; display: flex; align-items: center; }
  .run-foot .logo { position: static; font-size: 14px; }
  .run-foot .logo-mark { width: 9px; height: 9px; }
  .run-foot .rule { flex: 1; height: 1px; background: #777; margin: 0 8px; align-self: flex-end; margin-bottom: 4px; }
  .page-no { background: #1c1c1c; color: #fff; font-size: 11px; font-weight: 700; padding: 1px 3px; }

  .page-heading { position: absolute; left: 26px; font-size: 25px; line-height: 1.17; font-weight: 700; color: var(--ink); }
  .pill { position: absolute; left: 0; height: 27px; border-radius: 0 14px 14px 0; background: linear-gradient(90deg, var(--teal), var(--teal-light)); color: #fff; font-size: 10px; font-weight: 500; display: flex; align-items: center; padding-left: 26px; }
  .body-copy { position: absolute; font-size: 8.3px; line-height: 1.5; text-align: justify; color: var(--ink-soft); }

  .chart { position: absolute; left: 18px; width: 240px; height: 94px; }
  .stat { position: absolute; width: 150px; text-align: center; }
  .stat-ring { width: 93px; height: 93px; margin: 0 auto; border: 2.5px solid var(--teal); border-radius: 50%; display: flex; align-items: center; justify-content: center; font-size: 20px; font-weight: 700; background: #fff; }
  .stat-label { font-size: 8.5px; line-height: 1.25; margin-top: 9px; font-weight: 500; }

  .usp-list { position: absolute; left: 26px; top: 380px; display: flex; gap: 16px; list-style: none; font-size: 7.5px; font-weight: 700; }
  .usp-list li::before { content: ""; display: inline-block; width: 6px; height: 6px; border-radius: 50%; background: var(--ink); box-shadow: 0 0 0 2px var(--teal); margin-right: 6px; vertical-align: 0; }

  .price { position: absolute; left: 26px; font-size: 27px; font-weight: 700; color: var(--ink); }
  .price span { color: var(--teal); }
  .inclusions { position: absolute; left: 26px; list-style: none; font-size: 7.8px; font-weight: 500; }
  .inclusions li::before { content: ""; display: inline-block; width: 5px; height: 5px; border-radius: 50%; background: var(--ink); box-shadow: 0 0 0 2px var(--teal); margin-right: 9px; vertical-align: 1px; }
</style>
</head>
<body>
<div class="canvas">

  <div class="stage-label" style="left:378px;top:62px">Front Page</div>
  <div class="stage-label" style="left:831px;top:62px">Back Page</div>

  <!-- Cover -->
  <section class="page cover">
    <div class="logo"><span class="logo-mark"></span>Lanternvale</div>
    <div class="cover-address"><b>Address of property:</b><br>14 Rua das Flores<br>Lagos 8600, Algarve</div>
    <div class="cover-tab"></div>
    <div class="cover-band"></div>
    <div class="cover-band-edge"></div>
    <h1 class="cover-title">Property<br>Revenue Forecast</h1>
    <div class="cover-prepared">Prepared by Marta Ribeiro</div>
    <div class="photo" role="img" aria-label="Photo of the property: bright modern living room with large windows onto a garden" style="left:0;top:294px;width:386px;height:241px;background:linear-gradient(120deg,#e9ecea 0%,#cfd6d4 35%,#6f7b74 60%,#9fb08a 85%,#d9dfd6 100%)"></div>
    <div class="cover-footer">
      <span><i class="contact-dot"></i>+351 282 000 145</span><span class="sep">|</span>
      <span><i class="contact-dot"></i>info@lanternvale.pt</span><span class="sep">|</span>
      <span><i class="contact-dot"></i>www.lanternvale.pt</span>
    </div>
  </section>

  <!-- Back page -->
  <section class="page back">
    <div class="photo" role="img" aria-label="Alternate property photo: open-plan lounge and dining room with sea views" style="left:0;top:27px;width:338px;height:250px;background:linear-gradient(160deg,#bfc6cc 0%,#8d8f92 40%,#a98c6f 70%,#6b5a4a 100%)"></div>
    <div class="back-edge"></div>
    <div class="back-band"></div>
    <h2 class="back-title">Contact Us</h2>
    <div class="back-prepared">Prepared by Marta Ribeiro</div>
    <div class="logo"><span class="logo-mark"></span>Lanternvale</div>
    <div class="back-label">Address of property:</div>
    <ul class="back-contacts">
      <li><i class="contact-dot"></i>14 Rua das Flores</li>
      <li style="padding-left:12px">Lagos 8600, Algarve</li>
      <li><i class="contact-dot"></i>+351 282 000 145</li>
      <li><i class="contact-dot"></i>info@lanternvale.pt</li>
      <li><i class="contact-dot"></i>www.lanternvale.pt</li>
    </ul>
  </section>

  <!-- Page 01: figures -->
  <section class="page inner p1">
    <header class="run-head"><span class="run-title">Property Revenue Forecast</span><span class="run-by">Prepared by Marta Ribeiro</span></header>
    <h2 class="page-heading" style="top:72px">PROPERTY<br>FIGURES</h2>

    <div class="pill" style="top:159px;width:178px">Month by Month revenue</div>
    <svg class="chart" style="top:185px" viewBox="0 0 240 94">
      <g stroke="var(--grid)" stroke-width=".6"><line x1="22" y1="10" x2="236" y2="10"/><line x1="22" y1="32" x2="236" y2="32"/><line x1="22" y1="54" x2="236" y2="54"/><line x1="22" y1="76" x2="236" y2="76"/>
      <line x1="40" y1="10" x2="40" y2="84"/><line x1="80" y1="10" x2="80" y2="84"/><line x1="120" y1="10" x2="120" y2="84"/><line x1="160" y1="10" x2="160" y2="84"/><line x1="200" y1="10" x2="200" y2="84"/></g>
      <path d="M22 30 C50 22,70 30,90 50 S130 40,160 36 S200 8,236 22 L236 84 L22 84Z" fill="#e3e9ec"/>
      <path d="M22 30 C50 22,70 30,90 50 S130 40,160 36 S200 8,236 22" fill="none" stroke="#8c959a" stroke-width="1.4"/>
      <circle cx="205" cy="13" r="4" fill="var(--teal)"/><line x1="205" y1="13" x2="205" y2="84" stroke="var(--teal)" stroke-width=".6"/>
      <g font-size="5" fill="#888"><text x="4" y="12">400</text><text x="4" y="34">300</text><text x="4" y="56">200</text><text x="4" y="78">100</text>
      <text x="34" y="92">Mon</text><text x="74" y="92">Tue</text><text x="113" y="92">Wed</text><text x="154" y="92">Thu</text><text x="196" y="92">Fri</text></g>
    </svg>

    <div class="pill" style="top:309px;width:178px">Average daily rate forecast</div>
    <svg class="chart" style="top:328px" viewBox="0 0 240 94">
      <g stroke="var(--grid)" stroke-width=".6"><line x1="22" y1="10" x2="236" y2="10"/><line x1="22" y1="32" x2="236" y2="32"/><line x1="22" y1="54" x2="236" y2="54"/><line x1="22" y1="76" x2="236" y2="76"/></g>
      <path d="M22 60 C40 48,55 50,70 56 S100 40,120 46 S150 60,170 44 S210 30,236 12 L236 84 L22 84Z" fill="#f7d3cd"/>
      <path d="M22 60 C40 48,55 50,70 56 S100 40,120 46 S150 60,170 44 S210 30,236 12" fill="none" stroke="var(--rose-line)" stroke-width="1.4"/>
      <g stroke="var(--rose-line)" stroke-width=".5"><line x1="50" y1="52" x2="50" y2="84"/><line x1="80" y1="52" x2="80" y2="84"/><line x1="110" y1="44" x2="110" y2="84"/><line x1="140" y1="50" x2="140" y2="84"/><line x1="170" y1="44" x2="170" y2="84"/><line x1="200" y1="32" x2="200" y2="84"/></g>
      <circle cx="146" cy="24" r="5" fill="#2a2d2f"/>
      <g font-size="5" fill="#888"><text x="4" y="12">600</text><text x="4" y="34">450</text><text x="4" y="56">300</text><text x="4" y="78">150</text>
      <text x="44" y="92">Jun</text><text x="84" y="92">Jul</text><text x="123" y="92">Aug</text><text x="164" y="92">Sep</text><text x="204" y="92">Oct</text></g>
    </svg>

    <div class="pill" style="top:450px;width:108px">Occupancy</div>
    <svg class="chart" style="top:468px" viewBox="0 0 240 94">
      <g stroke="var(--grid)" stroke-width=".6"><line x1="22" y1="10" x2="236" y2="10"/><line x1="22" y1="32" x2="236" y2="32"/><line x1="22" y1="54" x2="236" y2="54"/><line x1="22" y1="76" x2="236" y2="76"/>
      <line x1="40" y1="10" x2="40" y2="84"/><line x1="80" y1="10" x2="80" y2="84"/><line x1="120" y1="10" x2="120" y2="84"/><line x1="160" y1="10" x2="160" y2="84"/><line x1="200" y1="10" x2="200" y2="84"/></g>
      <path d="M22 36 C45 30,60 44,80 46 S120 36,150 44 S190 8,210 16 S228 36,236 34 L236 84 L22 84Z" fill="#e3e9ec"/>
      <path d="M22 36 C45 30,60 44,80 46 S120 36,150 44 S190 8,210 16 S228 36,236 34" fill="none" stroke="#8c959a" stroke-width="1.4"/>
      <circle cx="203" cy="13" r="4" fill="var(--teal)"/><line x1="203" y1="13" x2="203" y2="84" stroke="var(--teal)" stroke-width=".6"/>
      <g font-size="5" fill="#888"><text x="4" y="12">80</text><text x="4" y="34">60</text><text x="4" y="56">40</text><text x="4" y="78">20</text>
      <text x="34" y="92">Mon</text><text x="74" y="92">Tue</text><text x="113" y="92">Wed</text><text x="154" y="92">Thu</text><text x="196" y="92">Fri</text></g>
    </svg>

    <div class="stat" style="left:269px;top:78px"><div class="stat-ring">€ 1000</div><div class="stat-label">Total expected<br>annual revenue</div></div>
    <div class="stat" style="left:269px;top:210px"><div class="stat-ring">€ 500</div><div class="stat-label">Average<br>daily rate</div></div>
    <div class="stat" style="left:269px;top:342px"><div class="stat-ring">50%</div><div class="stat-label">Annual<br>occupancy rate</div></div>
    <div class="stat" style="left:269px;top:475px"><div class="stat-ring">60%</div><div class="stat-label">ROI</div></div>

    <footer class="run-foot"><div class="logo"><span class="logo-mark"></span>Lanternvale</div><span class="rule"></span><span class="page-no">01</span></footer>
  </section>

  <!-- Page 02: intro -->
  <section class="page inner p2">
    <header class="run-head"><span class="run-title">Property Revenue Forecast</span><span class="run-by">Prepared by Marta Ribeiro</span></header>
    <h2 class="page-heading" style="top:72px">LANTERNVALE</h2>
    <p class="body-copy" style="left:26px;top:112px;width:374px">Lorem Ipsum is simply dummy text of the printing and typesetting industry. Lorem Ipsum has been the industry's standard dummy text ever since the 1500s, when an unknown printer took a galley of type and scrambled it to make a type specimen book. It has survived not only five centuries, but also the leap into electronic typesetting, remaining essentially unchanged. It was popularised in the 1960s with the release of Letraset sheets containing Lorem Ipsum passages, and more recently with desktop publishing software like Aldus PageMaker including versions of Lorem Ipsum.</p>
    <div class="pill" style="top:233px;width:166px">WHY CHOOSE US</div>
    <p class="body-copy" style="left:26px;top:262px;width:374px">It is a long established fact that a reader will be distracted by the readable content of a page when looking at its layout. The point of using Lorem Ipsum is that it has a more-or-less normal distribution of letters, as opposed to using 'Content here, content here', making it look like readable English. Many desktop publishing packages and web page editors now use Lorem Ipsum as their default model text, and a search for 'lorem ipsum' will uncover many web sites still in their infancy. Various versions have evolved over the years, sometimes by accident, sometimes on purpose (injected humour and the like).</p>
    <ul class="usp-list"><li>MAKE MORE MONEY</li><li>STRESS FREE</li><li>COMPLETE FLEXIBILITY</li></ul>
    <div class="photo" role="img" aria-label="Photo of a furnished lounge with white sofa and grey armchair" style="left:0;top:402px;width:409px;height:180px;background:linear-gradient(180deg,#e8e8e6 0%,#d4d2ce 55%,#9c948a 80%,#c9c3bb 100%)"></div>
    <footer class="run-foot"><div class="logo"><span class="logo-mark"></span>Lanternvale</div><span class="rule"></span><span class="page-no">02</span></footer>
  </section>

  <div class="stage-label" style="left:602px;top:1393px">Inner pages</div>

  <!-- Page 03: setup -->
  <section class="page inner p3">
    <header class="run-head"><span class="run-title">Property Revenue Forecast</span><span class="run-by">Prepared by Marta Ribeiro</span></header>
    <h2 class="page-heading" style="top:69px;font-size:24px">LANTERNVALE<br>SETUP SERVICE</h2>
    <p class="body-copy" style="left:26px;top:150px;width:190px">Lorem Ipsum is simply dummy text of the printing and typesetting industry. Lorem Ipsum has been the industry's standard dummy text ever since the 1500s, when an unknown printer took a galley of type and scrambled it to make a type specimen book. It has survived not only five centuries, but also the leap into electronic typesetting, remaining essentially unchanged. It was popularised in the 1960s with the release of Letraset sheets containing Lorem Ipsum passages, and more recently with desktop publishing software like Aldus PageMaker including versions of Lorem Ipsum.</p>
    <div class="price" style="top:326px"><span>€495</span> set price</div>
    <div class="pill" style="top:381px;width:145px">INCLUSIONS</div>
    <ul class="inclusions" style="top:420px;line-height:19.5px">
      <li>Lorem Ipsum is simply dummy text</li>
      <li>Contrary to popular belief, Lorem Ipsum</li>
      <li>There are many variations of passages</li>
      <li>Lorem Ipsum is simply dummy text</li>
      <li>Contrary to popular belief, Lorem Ipsum</li>
      <li>There are many variations of passages</li>
      <li>Lorem Ipsum is simply dummy text</li>
    </ul>
    <div class="photo" role="img" aria-label="Photo of a villa terrace and pool at dusk" style="left:227px;top:72px;width:177px;height:514px;background:linear-gradient(180deg,#3b2f52 0%,#7a4a6a 30%,#2b2a33 55%,#2e6f86 72%,#4a3a32 100%)"></div>
    <footer class="run-foot"><div class="logo"><span class="logo-mark"></span>Lanternvale</div><span class="rule"></span><span class="page-no">03</span></footer>
  </section>

  <!-- Page 04: management -->
  <section class="page inner p4">
    <header class="run-head"><span class="run-title">Property Revenue Forecast</span><span class="run-by">Prepared by Marta Ribeiro</span></header>
    <h2 class="page-heading" style="top:69px;font-size:24px">LANTERNVALE<br>PROPERTY<br>MANAGEMENT</h2>
    <p class="body-copy" style="left:26px;top:180px;width:196px">Lorem Ipsum is simply dummy text of the printing and typesetting industry. Lorem Ipsum has been the industry's standard dummy text ever since the 1500s, when an unknown printer took a galley of type and scrambled it to make a type specimen book. It has survived not only five centuries, but also the leap into electronic typesetting, remaining essentially unchanged. It was popularised in the 1960s with the release of Letraset sheets containing Lorem Ipsum passages, and more recently with desktop publishing software like Aldus PageMaker including versions of Lorem Ipsum.</p>
    <div class="price" style="top:356px"><span>25%</span> set price</div>
    <div class="pill" style="top:409px;width:145px">INCLUSIONS</div>
    <ul class="inclusions" style="top:444px;line-height:15.6px">
      <li>Lorem Ipsum is simply dummy text</li>
      <li>Contrary to popular belief, Lorem Ipsum</li>
      <li>There are many variations of passages</li>
      <li>Lorem Ipsum is simply dummy text</li>
      <li>Contrary to popular belief, Lorem Ipsum</li>
      <li>There are many variations of passages</li>
      <li>Lorem Ipsum is simply dummy text</li>
      <li>There are many variations of passages</li>
      <li>Lorem Ipsum is simply dummy text</li>
    </ul>
    <div class="photo" role="img" aria-label="Photo of a brick house with white columns and a green lawn" style="left:232px;top:79px;width:177px;height:507px;background:linear-gradient(180deg,#6fa6dc 0%,#a9c8e6 22%,#9b5a44 40%,#d9d3c8 55%,#4f7a33 70%,#7fae3f 100%)"></div>
    <footer class="run-foot"><div class="logo"><span class="logo-mark"></span>Lanternvale</div><span class="rule"></span><span class="page-no">04</span></footer>
  </section>

  <div class="stage-label" style="left:602px;top:2139px">Inner pages</div>
</div>
</body>
</html>
```